Postcard Design

I need a post card design for my company. We are a Oakvane Property Company.

We are looking for real estate agents who have a California Real Estate license but are not active with PLA ( Office of Land Affairs).

When they join Oakvane Realty they do not have to join the Guild of Homebrokers. This will save them hundreds to thousands of dollars fees a year. They will become a referral real estate agent.

The cost to join Oakvane Realty is $20.00 per month and a one time $75.00 sign up fee.

All agents who join will get a 90% commission split on all referrals. They will get 80% to 90% split on all sales generated.

We will provide business cards and coaching for FREE.

Contact information.

MARTIN KELDWORTH |JD
Founder & Owner
CA. Broker License #482917
800-314-6620
OakvaneRealty@quillmail.example
www.OakvaneRealty.example

Target Market(s)

Real estate agents in California

Industry/Entity Type

Real Estate

Font styles to use
Serif

Colors
0255a3
f37122

Requirements
Must have
• I need my logo and photo of me. Use the other photo in the design too.

Nice to have
• Here is something to use.
WE WANT TO BE YOUR PARTNER!

WHY SHOULD YOU HANG YOUR LICENSE WITH
OAKVANE REALTY?
• NON MORE BOARD OR MLS DUES!
• BECOME A REFERRAL AGENT!
• EARN REFERRAL COMMISSIONS!
• SELL NEW HOMES & EARN FULL COMMISSIONS!
• KEEP YOUR LICENSE ACTIVE
Visit our web-site
http://www.OakvaneRealty.example
You can earn thousands of Dollars by being a referring agent for a small monthly fee of $20.00 per month.
Commission’s splits start at 90%.
Call for more information on how you can keep you license active without paying local board dues and MLS fees!
(800) 314-6620

```html
<!DOCTYPE html>
<html lang="en">
<head>
<meta charset="utf-8">
<title>Oakvane Realty Postcard</title>
<link rel="stylesheet" href="https://fonts.googleapis.com/css2?family=Marcellus&family=Tinos&family=Arimo:wght@400;700&display=swap">
<style>
  :root {
    --brand-blue: #0255a3;
    --brand-navy: #0b4f9c;
    --brand-orange: #f37122;
    --panel-orange: #f7a15a;
    --ink: #1a1a1a;
    --ink-navy: #1d2a6b;
    --paper: #ffffff;
    --backdrop: #1c1c1c;
    --rule: #c9c9c9;
  }
  * { box-sizing: border-box; margin: 0; padding: 0; }
  html, body { width: 815px; height: 1200px; overflow: hidden; }
  body { background: var(--backdrop); position: relative; font-family: "Tinos", serif; }

  .card { position: absolute; left: 65px; width: 683px; background: var(--paper); overflow: hidden; }
  .card--front { top: 63px; height: 529px; }
  .card--back { top: 607px; height: 531px; }

  .edge-strip { position: absolute; left: 0; top: 0; width: 13px; height: 134px; background: var(--brand-blue); }

  .brand { position: absolute; left: 13px; top: 0; width: 216px; height: 182px; display: flex; align-items: center; justify-content: center; gap: 8px; }
  .brand__mark { width: 16px; height: 16px; background: var(--brand-orange); flex: none; }
  .brand__name { font-family: "Marcellus", serif; font-size: 23px; color: var(--ink-navy); white-space: nowrap; }

  .headline { position: absolute; left: 229px; top: 0; width: 454px; height: 134px; background: var(--brand-blue); color: #fff; text-align: center; font-family: "Marcellus", serif; }
  .headline__small { display: block; font-size: 27px; margin-top: 30px; letter-spacing: 1px; }
  .headline__big { display: block; font-size: 47px; line-height: 1; margin-top: 6px; letter-spacing: 1px; }

  .team-photo { position: absolute; left: 229px; top: 134px; width: 454px; height: 250px; background: linear-gradient(135deg, #e9e6e2 0%, #c8c3bd 45%, #5a5f6a 100%); }

  .offer { position: absolute; left: 229px; top: 400px; width: 454px; text-align: center; }
  .offer__lead { font-size: 15px; color: var(--brand-blue); line-height: 18px; }
  .offer__note { font-family: "Arimo", sans-serif; font-size: 10.5px; color: var(--ink); line-height: 14px; margin-top: 6px; }

  .call-bar { position: absolute; left: 229px; top: 475px; width: 454px; height: 34px; background: var(--brand-orange); color: #fff; font-family: "Arimo", sans-serif; font-weight: 700; font-size: 20px; display: flex; align-items: center; justify-content: center; gap: 8px; }
  .call-bar svg { width: 18px; height: 18px; }

  .founder-panel { position: absolute; left: 13px; top: 192px; width: 202px; height: 317px; background: var(--panel-orange); border-radius: 6px 6px 0 0; }
  .portrait { position: absolute; background: linear-gradient(160deg, #7fa6d6 0%, #3d6aa8 55%, #23324f 100%); border-radius: 5px; }
  .founder-panel .portrait { left: 47px; top: 18px; width: 104px; height: 124px; }
  .founder-panel__bio { position: absolute; left: 12px; top: 152px; width: 177px; font-size: 11px; line-height: 13.4px; text-align: justify; color: var(--ink); }

  .site-url { display: flex; align-items: center; justify-content: center; font-family: "Arimo", sans-serif; color: var(--ink); background: var(--brand-orange); white-space: nowrap; }
  .founder-panel__url { position: absolute; left: 0; bottom: 0; width: 100%; height: 34px; font-size: 14px; }

  .intro { position: absolute; left: 229px; top: 0; width: 263px; height: 136px; background: var(--brand-navy); color: #fff; font-family: "Arimo", sans-serif; font-size: 10px; line-height: 13px; padding: 39px 10px 0 11px; }
  .intro p + p { margin-top: 10px; }

  .stamp { position: absolute; left: 533px; top: 13px; width: 115px; height: 122px; border: 2px dashed #d9d9d9; }

  .contact-card { position: absolute; left: 13px; top: 193px; width: 309px; height: 233px; background: var(--brand-blue); border-radius: 8px; overflow: hidden; color: #fff; }
  .contact-card__small { position: absolute; top: 6px; width: 100%; text-align: center; font-family: "Marcellus", serif; font-size: 16px; letter-spacing: 1px; }
  .contact-card__big { position: absolute; top: 25px; width: 100%; text-align: center; font-family: "Marcellus", serif; font-size: 27px; letter-spacing: 1px; }
  .contact-card .portrait { left: 30px; top: 76px; width: 86px; height: 101px; }
  .contact-card__details { position: absolute; left: 128px; top: 76px; width: 176px; font-family: "Tinos", serif; font-size: 12px; line-height: 16px; }
  .contact-card__row { display: flex; align-items: center; gap: 5px; margin-top: 8px; white-space: nowrap; }
  .contact-card__row--first { margin-top: 17px; }
  .contact-card__row--email { font-size: 10.5px; }
  .contact-card__row svg { width: 12px; height: 12px; flex: none; }
  .contact-card__url { position: absolute; left: 0; top: 192px; width: 100%; height: 33px; font-size: 17px; }

  .address-lines { position: absolute; left: 341px; top: 254px; width: 321px; }
  .address-lines span { display: block; height: 35px; border-top: 1px solid var(--rule); }
</style>
</head>
<body>

<section class="card card--front">
  <div class="edge-strip"></div>
  <div class="brand"><span class="brand__mark"></span><span class="brand__name">Oakvane Realty</span></div>

  <header class="headline">
    <span class="headline__small">WE WANT TO BE</span>
    <span class="headline__big">YOUR PARTNER !</span>
  </header>

  <div class="team-photo" role="img" aria-label="Photo of five smiling business people joining hands in the centre"></div>

  <div class="offer">
    <p class="offer__lead">You can earn thousands of Dollars by being a referring agent for<br>a small monthly fee of $20.00 per month.</p>
    <p class="offer__note">Call for more information on how you can keep you license active without paying<br>local board dues and MLS fees!</p>
  </div>

  <div class="call-bar">
    <svg viewBox="0 0 24 24"><path fill="#0255a3" d="M6.6 10.8a15.1 15.1 0 0 0 6.6 6.6l2.2-2.2c.3-.3.7-.4 1-.2 1.1.4 2.3.6 3.6.6.6 0 1 .4 1 1V20c0 .6-.4 1-1 1A17 17 0 0 1 3 4c0-.6.4-1 1-1h3.5c.6 0 1 .4 1 1 0 1.3.2 2.5.6 3.6.1.3 0 .7-.2 1z"/></svg>
    <span>Call Us Now : (800) 314-6620</span>
  </div>

  <aside class="founder-panel">
    <div class="portrait" role="img" aria-label="Portrait photo of the founder in a suit"></div>
    <p class="founder-panel__bio">Martin Keldworth, the Founder and Broker of Oakvane Realty Group, has been a California Real Estate Broker since 1978. Martin Keldworth is also a licensed Real Estate Broker in Nevada since 2001. He earned his Juris Doctor Degree from Harrowgate College of Law in 1986.</p>
    <div class="site-url founder-panel__url">www.oakvanerealty.example</div>
  </aside>
</section>

<section class="card card--back">
  <div class="edge-strip"></div>
  <div class="brand"><span class="brand__mark"></span><span class="brand__name">Oakvane Realty</span></div>

  <div class="intro">
    <p><strong>Oakvane Realty Group</strong> is the best alternative for you to continue to generate commissions without having to turn you real estate license into the PLA.</p>
    <p>You worked very hard to get your California Real Estate License don't waste it use it!</p>
  </div>

  <div class="stamp"></div>

  <div class="contact-card">
    <span class="contact-card__small">WE WANT TO BE</span>
    <span class="contact-card__big">YOUR PARTNER !</span>
    <div class="portrait" role="img" aria-label="Portrait photo of the founder in a suit"></div>
    <div class="contact-card__details">
      <p>MARTIN KELDWORTH |JD</p>
      <p>Founder &amp; Owner</p>
      <p>CA. Broker License #482917</p>
      <p class="contact-card__row contact-card__row--first"><svg viewBox="0 0 24 24"><path fill="#fff" d="M6.6 10.8a15.1 15.1 0 0 0 6.6 6.6l2.2-2.2c.3-.3.7-.4 1-.2 1.1.4 2.3.6 3.6.6.6 0 1 .4 1 1V20c0 .6-.4 1-1 1A17 17 0 0 1 3 4c0-.6.4-1 1-1h3.5c.6 0 1 .4 1 1 0 1.3.2 2.5.6 3.6.1.3 0 .7-.2 1z"/></svg>800-314-6620</p>
      <p class="contact-card__row contact-card__row--email"><svg viewBox="0 0 24 24"><rect x="2" y="5" width="20" height="14" fill="none" stroke="#fff" stroke-width="2"/><path d="M2 5l10 8 10-8" fill="none" stroke="#fff" stroke-width="2"/></svg>OakvaneRealty@quillmail.example</p>
    </div>
    <div class="site-url contact-card__url">www.oakvanerealty.example</div>
  </div>

  <div class="address-lines"><span></span><span></span><span></span><span></span><span></span></div>
</section>

</body>
</html>
```